Lesson Lantern

LessonLantern.net will be a place for people looking for information, resources, and advisement to start or continue their education. We want a friendly, inviting site design that makes finding what potential students are looking for simple and easy to navigate. We are not committed to the colors of the logo, so variations on the color scheme are welcome.

Text instructions based on the wireframe: For the site's homepage we'd like a banner at the very top for our Logo and white space to the right of it. See attachments for logo + wireframe. Below that would be navigation. Below that split into 2/3 on the left we would have home page content, and 1/3 on the right we would have the lead form. At the bottom of the page we would have a space for types of degrees, then a footer with copyright info + site info.

See wireframes for additional page layouts.

Industry/Entity Type

Education

Requirements
Must have
• At minimum we are looking for three pages: homepage, choose your degree path page, and content page.
Nice to have
• -White space is appreciated
-Variations on the color scheme are welcome, we are not married to the existing logo's color scheme.

```html
<!DOCTYPE html>
<html lang="en">
<head>
<meta charset="utf-8">
<title>Lesson Lantern – Home</title>
<link href="https://fonts.googleapis.com/css2?family=Arimo:wght@400;700&family=Open+Sans:wght@400;600;700&family=Archivo+Black&display=swap" rel="stylesheet">
<style>
:root{
  --green:#8ca80e;
  --green-light:#c9dc52;
  --green-deep:#5f7a12;
  --ink:#4f4f4f;
  --text:#5a5a5a;
  --muted:#8a8a8a;
  --panel:#efeee3;
  --field:#c9c6b8;
  --dark:#1f1f1f;
  --footer:#404040;
  --teal:#2f6b7d;
  --white:#ffffff;
}
*{margin:0;padding:0;box-sizing:border-box}
html,body{width:932px;height:1200px;overflow:hidden}
body{font-family:"Arimo",Arial,sans-serif;color:var(--text);background:var(--white)}
.page{position:relative;width:932px;height:1200px;overflow:hidden}
.abs{position:absolute}

.header{left:0;top:0;width:932px;height:93px;background:linear-gradient(#fff,#f2f2f2)}
.brand{left:79px;top:38px;font-family:"Open Sans",sans-serif;font-weight:700;font-size:30px;color:var(--ink);letter-spacing:-.5px;display:flex;align-items:center;gap:8px}
.brand-mark{width:18px;height:18px;background:var(--green-light)}
.follow{left:724px;top:12px;font-size:8.5px;font-weight:700;color:#666}
.social{top:9px;width:15px;height:15px;border-radius:2px;background:#4a4a4a}
.phone-box{left:684px;top:36px;width:50px;height:50px;border-radius:6px;background:linear-gradient(#f4f4f4,#cfcfcf);box-shadow:0 1px 3px rgba(0,0,0,.3)}
.tollfree{left:739px;top:45px;font-family:"Open Sans",sans-serif;font-size:11.5px;color:#333}
.toll-number{left:738px;top:58px;font-size:16px;font-weight:700;color:var(--teal);letter-spacing:.3px}

.backdrop{left:0;top:93px;width:932px;height:1015px;background:radial-gradient(ellipse at 10% 20%,#6f8d14 0%,#a7c22c 25%,#d9e88c 55%,#eef3c8 80%)}
.panel{left:61px;top:93px;width:810px;height:1015px;background:var(--panel);box-shadow:0 0 4px rgba(0,0,0,.2)}

.ribbon{top:115px;width:30px;height:40px;background:#111}
.navbar{left:50px;top:105px;width:832px;height:39px;background:var(--dark)}
.nav-home{left:297px;top:96px;width:81px;height:42px;background:linear-gradient(#fff,#e9e9e9)}
.nav-item{top:116px;font-family:"Open Sans",sans-serif;font-size:11.5px;color:#e8e8e8;letter-spacing:.4px}
.nav-item.active{color:#333}
.nav-sep{top:111px;width:0;height:28px;border-left:1px dotted #555}

.slider{left:72px;top:150px;width:786px;height:322px;background:#f4f4f2;box-shadow:0 1px 3px rgba(0,0,0,.25)}
.slide{left:81px;top:152px;width:769px;height:283px;background:linear-gradient(115deg,#7a6a5a 0%,#3d3b39 30%,#2c3556 60%,#3c5692 78%,#b9b4aa 100%)}
.dot{top:449px;width:15px;height:15px;border-radius:50%;background:#9a9a9a}
.dot.on{background:#333}
.shelf{left:85px;top:472px;width:760px;height:24px}

.welcome-icon{left:95px;top:510px;width:37px;height:50px;border-radius:6px;background:#7d7d7d}
.welcome-title{left:143px;top:522px;font-family:"Open Sans",sans-serif;font-weight:600;font-size:26px;color:var(--ink)}
.welcome-title span,.accent{color:var(--green)}
.title-rule{height:3px;background:linear-gradient(90deg,#b5b5ab,rgba(181,181,171,0))}
.copy{font-size:10.2px;line-height:14.6px;color:var(--text);text-align:justify}
.btn-more{width:59px;height:18px;border-radius:3px;background:#2a2a2a;color:#fff;font-size:9px;font-weight:700;line-height:18px;text-align:center}
.why-icon{left:93px;top:764px;width:32px;height:50px;border-radius:4px;background:#8a8a8a}
.sub-title{font-family:"Open Sans",sans-serif;font-weight:600;font-size:14.6px;color:var(--ink)}
.divider{left:592px;top:509px;width:0;height:433px;border-left:1px solid #aaa}

.lead-icon{left:612px;top:509px;width:38px;height:40px;border-radius:4px;background:#9a9a9a}
.field{left:614px;width:217px;height:21px;background:var(--field);font-size:9.8px;color:#333;padding:5px 6px}
.select-arrow{left:808px;top:682px;width:23px;height:21px;border-left:1px solid #eee}
.submit{left:614px;top:783px;width:61px;height:19px;border-radius:3px;background:#1d1d1d;color:#f5e463;font-size:10px;font-weight:700;text-align:center;line-height:19px}
.or{left:708px;top:780px;font-family:"Archivo Black",sans-serif;font-size:32px;color:#d8d7cc}
.call-box{left:608px;top:827px;width:238px;height:110px;background:linear-gradient(#fff,#ececec);border:1px solid #ddd}
.call-photo{left:609px;top:828px;width:73px;height:108px;background:linear-gradient(160deg,#f3a36c,#e86a1e 55%,#d9d9d9)}
.click{left:698px;top:826px;font-family:"Archivo Black",sans-serif;font-size:35px;color:var(--green);letter-spacing:1px}
.call-now{left:704px;top:868px;font-family:"Archivo Black",sans-serif;font-size:13px;color:#222;letter-spacing:1px}
.call-text{left:689px;top:886px;font-size:8.8px;line-height:13px;color:#222}
.call-number{left:689px;top:912px;font-size:19px;font-weight:700;color:#555}

.degrees-box{left:82px;top:981px;width:766px;height:107px;border-radius:5px;background:#f2f2f0;border:2px solid #fff;box-shadow:0 0 3px rgba(0,0,0,.25)}
.cert{top:995px;width:96px;height:73px;border:4px solid;background:#fbfaf4}

.footer{left:0;top:1108px;width:932px;height:92px;background:var(--footer)}
.footer-brand{left:73px;top:1146px;font-family:"Open Sans",sans-serif;font-weight:600;font-size:22px;color:#ddd}
.footer-links{left:300px;top:1138px;font-size:10px;color:#ccc;word-spacing:2px}
.footer-copy{left:295px;top:1155px;font-size:10px;color:#ccc}
.footer-address{right:75px;top:1122px;font-size:9.8px;line-height:16.3px;color:#bbb;text-align:right}
.footer-address b{color:#bbb}
</style>
</head>
<body>
<div class="page">
  <header class="abs header"></header>
  <div class="abs brand"><span>Lesson Lantern</span><span class="brand-mark"></span></div>
  <div class="abs follow">Follow Us on :</div>
  <div class="abs social" style="left:799px"></div>
  <div class="abs social" style="left:817px"></div>
  <div class="abs social" style="left:835px"></div>
  <div class="abs phone-box">
    <svg width="50" height="50" viewBox="0 0 50 50"><rect x="11" y="11" width="28" height="28" rx="3" fill="#6b6b6b"/><rect x="16" y="16" width="10" height="18" rx="1" fill="#eee"/><rect x="29" y="16" width="6" height="18" rx="1" fill="#eee"/></svg>
  </div>
  <div class="abs tollfree">CALL US TOLL-FREE</div>
  <div class="abs toll-number">123 .456 .7890</div>

  <div class="abs backdrop" role="img" aria-label="Soft green leaf background"></div>
  <div class="abs panel"></div>

  <div class="abs ribbon" style="left:27px;clip-path:polygon(0 0,100% 0,100% 100%,0 100%,35% 50%)"></div>
  <div class="abs ribbon" style="left:875px;clip-path:polygon(0 0,100% 0,65% 50%,100% 100%,0 100%)"></div>
  <nav class="abs navbar"></nav>
  <div class="abs nav-home"></div>
  <div class="abs nav-item active" style="left:322px">HOME</div>
  <div class="abs nav-item" style="left:401px">ABOUT US</div>
  <div class="abs nav-sep" style="left:475px"></div>
  <div class="abs nav-item" style="left:496px">SERVICES</div>
  <div class="abs nav-sep" style="left:569px"></div>
  <div class="abs nav-item" style="left:590px">DEGREES</div>
  <div class="abs nav-sep" style="left:661px"></div>
  <div class="abs nav-item" style="left:687px">FAQ’S</div>
  <div class="abs nav-sep" style="left:741px"></div>
  <div class="abs nav-item" style="left:763px">CONTACT US</div>

  <div class="abs slider"></div>
  <div class="abs slide" role="img" aria-label="Student reading a book on the floor beside library shelves"></div>
  <div class="abs dot on" style="left:425px"></div>
  <div class="abs dot" style="left:446px"></div>
  <div class="abs dot" style="left:467px"></div>
  <div class="abs dot" style="left:487px"></div>
  <div class="abs dot" style="left:508px"></div>
  <svg class="abs shelf" viewBox="0 0 760 24" preserveAspectRatio="none"><path d="M0 24 Q380 -4 760 24 Z" fill="#d6d6c8"/></svg>

  <div class="abs welcome-icon" role="img" aria-label="Welcome tag icon"></div>
  <h1 class="abs welcome-title">Welcome - <span>Lesson Lantern</span></h1>
  <div class="abs title-rule" style="left:244px;top:559px;width:60px"></div>
  <p class="abs copy" style="left:88px;top:566px;width:479px">Curabitur mattis sem tincidunt arcu gravida aliquet. In hac habitasse platea dictumst. Class aptent taciti sociosqu ad litora torquent per conubia nostra, per inceptos himenaeos. Quisque nisi risus, varius et sodales vitae, imperdiet vel sapien. In et est a elit luctus lacinia eu vel sapien. Mauris pulvinar venenatis elit nec egestas.</p>
  <p class="abs copy" style="left:88px;top:639px;width:479px">Proin hendrerit euismod velit, non imperdiet dolor aliquam et. Nullam id nulla vitae sem congue ultrices eu id sapien. Donec et dolor ac dui suscipit pellentesque. Pellentesque habitant morbi tristique senectus et netus et malesuada fames ac turpis egestas. Nunc at velit sapien. Aenean iaculis odio quis lacus bibendum volutpat lobortis libero tincidunt. Nullam ut risus turpis. In nulla tellus, semper ut ornare et, adipiscing sed arcu.</p>
  <div class="abs btn-more" style="left:508px;top:724px">Read more ▸</div>

  <div class="abs why-icon" role="img" aria-label="Figure with question mark icon"></div>
  <h2 class="abs sub-title" style="left:130px;top:778px">Why <span class="accent">Lesson Lantern ??</span></h2>
  <div class="abs title-rule" style="left:131px;top:804px;width:150px"></div>
  <p class="abs copy" style="left:88px;top:820px;width:479px">Pellentesque habitant morbi tristique senectus et netus et malesuada fames ac turpis egestas. Nunc at velit sapien. Aenean iaculis odio quis lacus bibendum volutpat lobortis libero tincidunt. Nullam ut risus turpis. In nulla tellus, semper ut ornare et, adipiscing sed arcu.<br>Quisque nisi risus, varius et sodales vitae, imperdiet vel sapien. In et est a elit luctus lacinia eu vel sapien. Mauris pulvinar venenatis elit nec egestas.</p>
  <div class="abs btn-more" style="left:508px;top:907px">Read more ▸</div>

  <div class="abs divider"></div>

  <div class="abs lead-icon" role="img" aria-label="Person at laptop icon"></div>
  <h2 class="abs sub-title" style="left:658px;top:515px">Lead <span class="accent">Form</span></h2>
  <div class="abs title-rule" style="left:658px;top:536px;width:95px"></div>
  <p class="abs copy" style="left:615px;top:553px;width:211px;font-size:9.8px;line-height:13px;color:#777">Send us a quick email with any questions or concerns you may have about your potential case.</p>
  <div class="abs field" style="top:600px">Your Name</div>
  <div class="abs field" style="top:628px">Your Email Address</div>
  <div class="abs field" style="top:656px">Your Phone No.</div>
  <div class="abs field" style="top:682px">Interested In</div>
  <svg class="abs select-arrow" viewBox="0 0 23 21"><path d="M8 9h7l-3.5 4z" fill="#333"/></svg>
  <div class="abs field" style="top:710px;height:60px">Provide Your Education Details.</div>
  <div class="abs submit">Submit</div>
  <div class="abs or">OR</div>

  <div class="abs call-box"></div>
  <div class="abs call-photo" role="img" aria-label="Hand holding an orange telephone handset"></div>
  <div class="abs click">CLICK</div>
  <div class="abs call-now">CALL-US-NOW</div>
  <div class="abs call-text">Have a question about your career ?<br>Click here to connect to our office.</div>
  <div class="abs call-number">123 .456 .7890</div>

  <h2 class="abs sub-title" style="left:122px;top:948px">List of <span class="accent">degrees</span></h2>
  <div class="abs title-rule" style="left:123px;top:972px;width:100px"></div>
  <div class="abs degrees-box"></div>
  <div class="abs cert" style="left:100px;border-color:#6b3a4a" role="img" aria-label="Sample degree certificate"></div>
  <div class="abs cert" style="left:222px;border-color:#f0ead6" role="img" aria-label="Sample degree certificate"></div>
  <div class="abs cert" style="left:344px;border-color:#9db3d6" role="img" aria-label="Sample degree certificate"></div>
  <div class="abs cert" style="left:468px;border-color:#d6a878" role="img" aria-label="Sample degree certificate"></div>
  <div class="abs cert" style="left:593px;border-color:#555" role="img" aria-label="Sample degree certificate"></div>
  <div class="abs cert" style="left:719px;border-color:#c4c4c4" role="img" aria-label="Sample degree certificate"></div>

  <footer class="abs footer"></footer>
  <div class="abs footer-brand">Lesson Lantern</div>
  <div class="abs footer-links">Home &nbsp;|&nbsp; About Us &nbsp;|&nbsp; Services &nbsp;|&nbsp; Degrees &nbsp;|&nbsp; FAQs &nbsp;|&nbsp; Contact</div>
  <div class="abs footer-copy">Copyright © 2011 - LessonLantern.net - All rights reserved. Terms and Privacy Policy</div>
  <div class="abs footer-address"><b>Address Line 1 with City</b><br><b>Address Line 2 with Country</b><br>Tel. : 123 . 456 . 7890<br>Email : info@lessonlantern.net</div>
</div>
</body>
</html>
```